Web Design for non-profit, Nautical themed

We are developing a web design for a non-profit organization. They are:

a non-profit 501©3 educational and service organization, grounded in the recognition that active engagement of the arts through can be an entry into growth and transformation. Our purpose is to develop and offer events that support this creative process bringing outstanding presenters to our town.

They are located in a beautiful coastal town and the client would like a "nautical" theme. This would include

- color palette of blue, green, possibly brown/beige, and possibly some deep red colors as accents. There is a file attached with some color palette ideas, but you don't have to choose from colors here.

- soothing, calm, clean professional look

- something in the background image that would indicate the four directions. This could be a compass or something similar.

- the client really likes this website:
http://www.thelarkmoorcenter.org/

Please see attached for:

- a basic sketch that shows the overall layout that we desire. Feel free to modify this slightly but not too much. File name is 01-sketch.psd

- placeholder content that can be used throughout your design

You can also use any of the stock photos found here:
http://www.pixvaultimages.com/search/lightbox/48207356#a9d1b72

Target Market(s)

Mainly white American women who are in their 40s or older. Professional, affluent, highly educated.

Industry/Entity Type

Nautical

Requirements
Must have
• - sidebar with event information. Each event should include date, headshot, title, brief description and a "Register" and "Read more" link. We don't have any real headshots so use ones from Internet for now.

- use the attached 01-sketch.psd file as your starting point.

```html
<!DOCTYPE html>
<html lang="en">
<head>
<meta charset="utf-8">
<title>Tidewater Dialogues Inc.</title>
<link href="https://fonts.googleapis.com/css2?family=Open+Sans:wght@400;600;700&family=Roboto+Condensed:wght@700&display=swap" rel="stylesheet">
<style>
:root{
  --navy:#13365a;
  --navy-dark:#0f2c4a;
  --teal:#00897a;
  --sea-top:#0f6f6a;
  --sea-bottom:#23a99a;
  --red:#8c1c1c;
  --ink:#1a1a1a;
  --grey-band:#ececec;
  --slide-grey:#b9b6bb;
  --white:#ffffff;
}
*{box-sizing:border-box;margin:0;padding:0}
html,body{width:1026px;height:1200px;overflow:hidden;background:var(--white)}
body{position:relative;font-family:"Open Sans",Arial,sans-serif;color:var(--ink)}
.abs{position:absolute}

/* top bar */
.topbar{left:0;top:0;width:1026px;height:30px;background:var(--navy)}
.social{display:flex;gap:6px}
.social span{width:20px;height:20px;border-radius:3px;display:block}
.sq-blue{background:#3b64a8}.sq-red{background:#c4302b}.sq-navy{background:#2f5f9a}
.topbar .social{position:absolute;left:98px;top:5px}
.contact-strip{position:absolute;right:98px;top:0;height:30px;display:flex;align-items:center;gap:18px;color:#fff;font-size:8.5px;font-weight:600}
.contact-strip div{display:flex;align-items:center;gap:6px}

/* header */
.brand{left:96px;top:60px;display:flex;align-items:center;gap:10px}
.brand-mark{width:46px;height:46px;background:#4a4a4a}
.brand-name{font-size:25px;line-height:27px;color:#4a4a4a;font-weight:400}
.login{left:695px;top:110px;width:52px;height:23px;background:var(--navy);color:#fff;font-size:9.5px;font-weight:700;display:flex;align-items:center;justify-content:center}
.search{left:758px;top:110px;width:169px;height:23px;border:1px solid #777;font-size:7px;font-weight:600;padding-left:8px;display:flex;align-items:center}
.search svg{position:absolute;right:5px;top:4px}

/* nav */
.nav{left:0;top:153px;width:1026px;height:25px;background:var(--navy)}
.nav ul{list-style:none;display:flex;align-items:center;height:25px;position:absolute;left:96px;color:#fff;font-size:10px;font-weight:700;letter-spacing:-.2px}
.nav li.sep{margin:0 7px}
.nav li.home{background:#fff;color:var(--navy);width:67px;height:29px;margin-top:-4px;display:flex;align-items:center;justify-content:center;margin-right:20px;border:1px solid #ccc;border-bottom:none}

/* hero */
.sea{left:0;top:178px;width:1026px;height:292px;background:linear-gradient(180deg,var(--sea-top),var(--sea-bottom) 60%,#1b8f86)}
.band{left:0;top:470px;width:1026px;height:138px;background:linear-gradient(180deg,#f4f4f4,var(--grey-band))}
.slide{left:96px;top:205px;width:831px;height:303px;background:radial-gradient(ellipse at 65% 55%,#e6e4e8 0%,#c9c6cb 45%,#9c999e 100%);box-shadow:0 18px 22px -10px rgba(0,0,0,.25)}
.caption{left:96px;top:241px;width:382px;height:88px;background:rgba(40,40,40,.82);color:#fff;padding:12px 13px}
.caption h2{font-family:"Roboto Condensed",Arial,sans-serif;font-size:15.5px;letter-spacing:.1px;margin-bottom:2px}
.caption p{font-size:12px;line-height:14px}
.dots{left:114px;top:482px;display:flex;gap:3px}
.dots span{width:7px;height:7px;background:#fff}
.dots span.on{background:var(--teal)}

/* content */
.col h3{font-size:14.5px;font-weight:700;color:var(--navy);letter-spacing:.3px;margin-bottom:8px;font-family:Verdana,"Open Sans",sans-serif}
.col p{font-size:9.6px;line-height:12.3px;margin-bottom:12px;width:200px}
.btn{display:inline-flex;align-items:center;justify-content:center;background:var(--navy);color:#fff;font-size:9px;font-weight:700;width:66px;height:22px}
.vrule{width:1px;background:#999;top:636px;height:284px}
.event-date{font-size:10px;color:#333}
.headshot{width:90px;height:106px;border:1px solid #bbb;padding:3px;background:#fff}
.headshot div{width:100%;height:100%}
.event-text{font-size:10px;line-height:11.6px;width:134px}
.red-btn{background:var(--red);color:#fff;font-size:8px;font-weight:600;width:65px;height:13px;display:flex;align-items:center;justify-content:center;margin-top:3px}
.dash{left:699px;top:790px;width:228px;border-top:1px dashed #aaa}

/* footer */
.footer{left:0;top:972px;width:1026px;height:201px;background:var(--teal);color:#fff}
.footer h4{font-size:15px;font-weight:400}
.fmenu li{list-style:none;font-size:7.5px;font-weight:700;margin-top:12.5px}
.frule{top:36px;width:1px;height:128px;background:rgba(255,255,255,.5)}
.tweet{display:flex;gap:8px;font-size:10px;line-height:12px}
.tweet .avatar{width:60px;height:24px;display:flex;align-items:center;gap:3px;margin-top:5px;font-size:7px;color:#3d3d3d}
.tweet .avatar span{width:12px;height:12px;background:#3d3d3d}
.fcontact div{display:flex;align-items:flex-start;gap:7px;font-size:10px;margin-bottom:9px}
.email-field{width:161px;height:25px;background:#f4f4f4;color:#222;font-size:10px;padding:6px 7px}
.subscribe{width:61px;height:21px;background:var(--navy);font-size:10px;display:flex;align-items:center;justify-content:center;margin-top:13px}
.bottombar{left:0;top:1173px;width:1026px;height:27px;background:var(--navy);color:#fff;font-size:9px;letter-spacing:1.6px;display:flex;align-items:center;justify-content:center}
</style>
</head>
<body>

<header class="abs topbar">
  <div class="social"><span class="sq-blue"></span><span class="sq-red"></span><span class="sq-navy"></span></div>
  <div class="contact-strip">
    <div><svg width="11" height="14" viewBox="0 0 11 14"><circle cx="5.5" cy="7.5" r="4" fill="none" stroke="#fff" stroke-width="2"/><rect x="4" y="0" width="3" height="3" fill="#fff"/></svg>your address here your address here</div>
    <div><svg width="13" height="13" viewBox="0 0 13 13"><path d="M2 1l3 0 1 3-2 1.5c1 2 2 3 3.5 3.5L9 7l3 1v3c-6 1-11-4-10-10z" fill="#fff"/></svg>123 456 7890 123</div>
    <div><svg width="13" height="11" viewBox="0 0 13 11"><path d="M0 4l6.5-4 6.5 4v7H0z" fill="#fff"/><path d="M0 4l6.5 4 6.5-4" fill="none" stroke="var(--navy)" stroke-width="1"/></svg>info@tidewaterdialogues.org</div>
  </div>
</header>

<div class="abs brand">
  <div class="brand-mark"></div>
  <div class="brand-name">Tidewater<br>Dialogues Inc.</div>
</div>
<div class="abs login">LOGIN</div>
<div class="abs search">SEARCH
  <svg width="15" height="15" viewBox="0 0 15 15"><circle cx="8.5" cy="6" r="4.8" fill="none" stroke="#333" stroke-width="1.4"/><path d="M5 9.5L1 13.5" stroke="#333" stroke-width="1.6"/></svg>
</div>

<nav class="abs nav">
  <ul>
    <li class="home">HOME</li>
    <li>ABOUT US</li><li class="sep">I</li>
    <li>CALENDAR</li><li class="sep">I</li>
    <li>DONATE</li><li class="sep">I</li>
    <li>TRAVEL INFORMATION</li><li class="sep">I</li>
    <li>CONTACT US</li>
  </ul>
</nav>

<div class="abs sea" role="img" aria-label="Calm turquoise sea surface"></div>
<div class="abs band"></div>
<div class="abs slide" role="img" aria-label="Close-up photograph of a silver compass showing the four directions"></div>
<div class="abs caption">
  <h2>CONVERSATIONS THAT COULD TRANSFORM YOUR LIFE</h2>
  <p><b>Tidewater Dialogues</b> is bringing together speakers from around the globe who are transforming our world.<br>Join us for an event that could change your life.</p>
</div>
<div class="abs dots"><span class="on"></span><span></span><span></span><span></span><span></span></div>

<section class="abs col" style="left:96px;top:634px">
  <h3>WHO WE ARE?</h3>
  <p>Some text here Some text here Some text here Some text here Some text here Some text here.</p>
  <p>Some text here Some text here Some text here Some text here Some text here Some text here Some text here Some text here Some text here Some text here Some text here Some text here Some text here Some text here Some text here Some text here Some text here Some text here Some text here Some text here Some text here Some text here Some text here Some text here Some text here Some text here Some text here Some text here Some text here Some text here Some text here Some text here Some text here</p>
  <p>Some text here Some text here Some text here Some text here Some text here Some text here Some text here.</p>
  <span class="btn">Read More...</span>
</section>
<div class="abs vrule" style="left:339px"></div>
<section class="abs col" style="left:398px;top:634px">
  <h3>WHAT WE DO?</h3>
  <p>Some text here Some text here Some text here Some text here Some text here Some text here.</p>
  <p>Some text here Some text here Some text here Some text here Some text here Some text here Some text here Some text here Some text here Some text here Some text here Some text here Some text here Some text here Some text here Some text here Some text here Some text here Some text here Some text here Some text here Some text here Some text here Some text here Some text here Some text here Some text here Some text here Some text here Some text here Some text here Some text here Some text here</p>
  <p>Some text here Some text here Some text here Some text here Some text here Some text here Some text here.</p>
  <span class="btn">Read More...</span>
</section>
<div class="abs vrule" style="left:642px"></div>

<section class="abs col" style="left:699px;top:634px">
  <h3>UPCOMING EVENTS</h3>
</section>
<div class="abs event-date" style="left:699px;top:657px">June 1, 2013</div>
<div class="abs headshot" style="left:699px;top:672px"><div role="img" aria-label="Headshot of a speaker" style="background:linear-gradient(160deg,#d9b47a,#b88a5a)"></div></div>
<div class="abs" style="left:794px;top:672px">
  <div class="event-text">Some text here Some text here Some text here Some text here Some text here Some text here Some text here Some text here Some text here Some text here Some text here Some text here Some text here Some text here Some text here Some text here</div>
  <div class="red-btn">Read More...</div>
</div>
<div class="abs dash"></div>
<div class="abs event-date" style="left:699px;top:799px">July 1, 2013</div>
<div class="abs headshot" style="left:699px;top:814px"><div role="img" aria-label="Headshot of a speaker" style="background:linear-gradient(160deg,#a08a7c,#2b3038)"></div></div>
<div class="abs" style="left:794px;top:815px">
  <div class="event-text">Some text here Some text here Some text here Some text here Some text here Some text here Some text here Some text here Some text here Some text here Some text here Some text here Some text here Some text here Some text here Some text here</div>
  <div class="red-btn">Read More...</div>
</div>

<footer class="abs footer">
  <div class="abs" style="left:96px;top:35px">
    <h4>Menu</h4>
    <ul class="fmenu"><li>ABOUT US</li><li>CALENDAR</li><li>DONATE</li><li>TRAVEL INFORMATION</li><li>CONTACT US</li></ul>
  </div>
  <div class="abs frule" style="left:223px"></div>
  <div class="abs" style="left:256px;top:35px">
    <h4>Recet Tweets</h4>
    <div class="tweet" style="margin-top:10px"><div class="avatar"><span></span>Tidewater</div><div>“Some text herre<br>Some text herre Some text herre”<br>(http://t.co/k7QmRw2Lxb</div></div>
    <div style="font-size:7px;margin:2px 0 0 170px">10 min ago</div>
    <div class="tweet" style="margin-top:12px"><div class="avatar"><span></span>Tidewater</div><div>“Some text herre<br>Some text herre Some text herre”<br>(http://t.co/k7QmRw2Lxb</div></div>
  </div>
  <div class="abs frule" style="left:507px"></div>
  <div class="abs fcontact" style="left:539px;top:35px">
    <h4 style="margin-bottom:9px">Contact us</h4>
    <div><svg width="13" height="13" viewBox="0 0 13 13"><path d="M2 1l3 0 1 3-2 1.5c1 2 2 3 3.5 3.5L9 7l3 1v3c-6 1-11-4-10-10z" fill="#fff"/></svg>123 45 678900</div>
    <div><svg width="13" height="11" viewBox="0 0 13 11"><path d="M0 4l6.5-4 6.5 4v7H0z" fill="#fff"/><path d="M0 4l6.5 4 6.5-4" fill="none" stroke="var(--teal)"/></svg>info@tidewaterdialogues.org</div>
    <div><svg width="13" height="18" viewBox="0 0 13 18"><circle cx="6.5" cy="10.5" r="5" fill="none" stroke="#fff" stroke-width="2.2"/><rect x="5" y="0" width="3" height="4" fill="#fff"/></svg><span style="line-height:10px">Your adress here Your adress<br>here Your adress here</span></div>
    <div class="social" style="margin-top:2px"><span class="sq-blue"></span><span class="sq-red"></span><span class="sq-navy"></span></div>
  </div>
  <div class="abs frule" style="left:723px"></div>
  <div class="abs" style="left:756px;top:35px">
    <h4 style="margin-bottom:10px">Sign up for our Newsletter</h4>
    <div class="email-field">Email address</div>
    <div class="subscribe">Subscribe</div>
  </div>
</footer>
<div class="abs bottombar">Copyright 2013 Tidewater Dialogues &nbsp;I&nbsp; AllRights Reserved.</div>

</body>
</html>
```